Weihnachtskarte und Silvesterkarte für Immobilienmakler
Zielgruppe
Wir sind Immobilienmakler.
Ziel: Objektakquise
Aufgabenstellung
Benötigen einen Flyer in 2 Versionen: Weihnachten und Silvester.
Rückseite identisch: Firma, Leistungen, Angebot
Vorderseite: Schick, Edel, Ansprechend.
Einmal mit Weihnachtsglückwünschen, Zweite Version mit Neujahrsglückwünschen.
Nicht zu bunt. Farben eher gold oder silber.
Textideen dürfen gerne eingebracht werden
folgende Infos sollten hervorgehen:
Wir kümmern uns um Ihre Immobilie:
- Verkauf
- Vermietung
- Hausmeisterservice
- Home Staging
- NEU ab 2019 Hausverwaltung
Infos unter www.nordhaus-kellbrunn.de
Bei Abschluss eines Auftrags schenken wir Ihnen eine 'Nuvo' als Weihnachtsgeschenk / Neujahrsgeschenk.
Aktion gültig bis 31.01.2019
Für eine unverbindliche Beratung stehen wir gerne zur Verfügung.
Wir freuen uns auf Ihren Anruf.

```html
<!DOCTYPE html>
<html lang="de">
<head>
<meta charset="utf-8">
<title>Kellbrunn – Weihnachts- und Neujahrskarte</title>
<link rel="stylesheet" href="https://fonts.googleapis.com/css2?family=Quicksand:wght@400;500;700&family=Kaushan+Script&family=Fredoka:wght@600&display=swap">
<style>
  :root{
    --navy:#124a7c;
    --navy-soft:#1b5a93;
    --gold:#b9954a;
    --gold-glow:rgba(185,149,74,.38);
    --white:#ffffff;
    --snow-glow:rgba(255,255,255,.22);
    --ink:#1f2d3d;
    --stage-a:#ececec;
    --stage-b:#dedede;
    --stage-c:#ebebeb;
  }
  *{margin:0;padding:0;box-sizing:border-box}
  html,body{width:1200px;height:2164px;overflow:hidden}
  body{font-family:"Quicksand",sans-serif;color:var(--ink);position:relative}

  .stage{position:absolute;left:0;width:1200px}
  .stage--christmas{top:0;height:697px;background:var(--stage-a)}
  .stage--spread{top:697px;height:697px;background:var(--stage-b)}
  .stage--newyear{top:1394px;height:770px;background:var(--stage-c)}

  .card{position:absolute;width:515px;height:515px;overflow:hidden}
  .card-holder{position:absolute;width:470px;height:470px;overflow:hidden;box-shadow:0 6px 18px rgba(0,0,0,.12)}
  .card-holder .card{transform:scale(.9126);transform-origin:0 0;left:0;top:0}

  /* Christmas front */
  .xmas-front{background:var(--navy)}
  .xmas-front .ornaments{position:absolute;left:0;top:0;width:515px;height:370px;
    background:
      radial-gradient(circle at 17% 20%,var(--snow-glow),transparent 13%),
      radial-gradient(circle at 42% 13%,var(--snow-glow),transparent 11%),
      radial-gradient(circle at 85% 13%,var(--snow-glow),transparent 11%),
      radial-gradient(ellipse at 62% 36%,rgba(255,255,255,.3),transparent 22%),
      radial-gradient(circle at 8% 45%,var(--gold-glow),transparent 6%),
      radial-gradient(circle at 90% 40%,var(--gold-glow),transparent 6%),
      radial-gradient(circle at 12% 88%,var(--gold-glow),transparent 6%),
      radial-gradient(circle at 92% 80%,var(--gold-glow),transparent 6%),
      radial-gradient(circle at 30% 30%,var(--gold-glow),transparent 5%),
      radial-gradient(circle at 75% 27%,var(--gold-glow),transparent 5%),
      linear-gradient(180deg,var(--navy-soft),var(--navy))}
  .xmas-front .greeting{position:absolute;left:0;width:515px;text-align:center;font-family:"Kaushan Script",cursive;line-height:1}
  .xmas-front .greeting--small{top:246px;font-size:40px;color:var(--white);padding-left:30px}
  .xmas-front .greeting--large{top:270px;font-size:74px;color:var(--gold);letter-spacing:-1px}
  .xmas-front .trees{position:absolute;left:0;top:362px;width:515px;height:75px;
    background:linear-gradient(180deg,rgba(255,255,255,0) 0%,rgba(255,255,255,.45) 55%,rgba(255,255,255,.9) 100%)}
  .xmas-front .landscape{position:absolute;left:0;top:370px;width:515px;height:145px}
  .brand{position:absolute;display:flex;align-items:center;gap:7px;font-family:"Quicksand",sans-serif;font-weight:700;color:var(--navy)}
  .brand__dot{width:20px;height:20px;border-radius:50%;background:var(--gold);flex:none}
  .xmas-front .brand{left:0;width:515px;justify-content:center;top:478px;font-size:18px}

  /* Back side */
  .back{background:var(--white)}
  .services{position:absolute;left:0;top:0;width:117px;height:515px;background:var(--gold)}
  .service{position:absolute;left:0;width:117px;text-align:center;color:var(--white);font-size:12px;font-weight:500;line-height:15px}
  .service svg{display:block;margin:0 auto 6px}
  .back .brand{left:146px;top:72px;font-size:23px}
  .back .brand .brand__dot{width:30px;height:30px}
  .back .brand small{display:block;font-size:9px;color:var(--gold);font-weight:700;letter-spacing:.2px}
  .lead{position:absolute;left:322px;top:24px;width:178px;font-size:15px;line-height:21px;color:var(--navy)}
  .gold{color:var(--gold)}
  .phone{position:absolute;left:322px;top:98px;display:flex;align-items:center}
  .phone__icon{width:24px;height:24px;border-radius:50%;background:var(--white);border:1.5px solid var(--navy);display:flex;align-items:center;justify-content:center;position:relative;z-index:1}
  .phone__number{background:var(--gold);color:var(--white);font-weight:700;font-size:13px;height:19px;line-height:19px;padding:0 10px 0 14px;margin-left:-6px;width:146px}
  .rule{position:absolute;height:1px;background:var(--navy)}
  .heading{position:absolute;left:140px;top:158px;width:345px;text-align:center;font-size:15px;font-weight:400;color:var(--navy)}
  .gift{position:absolute;left:140px;top:222px;font-size:9.5px;line-height:13px;color:var(--ink)}
  .gift p{margin-bottom:12px}
  .gift .link{color:var(--navy)}
  .bauble{position:absolute;left:361px;top:185px;width:66px;height:100px}
  .bauble__string{position:absolute;left:32px;top:0;width:0;height:26px;border-left:1.5px dotted var(--gold)}
  .bauble__cap{position:absolute;left:27px;top:24px;width:12px;height:8px;background:var(--gold);border-radius:2px}
  .bauble__ball{position:absolute;left:0;top:30px;width:66px;height:66px;border-radius:50%;background:var(--gold);color:var(--white);
    font-weight:700;font-size:12.5px;line-height:14px;text-align:center;display:flex;align-items:center;justify-content:center;transform:rotate(-10deg)}
  .portrait{position:absolute;left:362px;top:300px;width:178px;height:178px;border-radius:50%;
    background:radial-gradient(circle at 45% 40%,#d4d6d9,#a4a8ae 65%,#7d828a)}
  .invite{position:absolute;left:140px;top:358px;width:212px;text-align:center;font-size:12.5px;line-height:16px;color:var(--navy)}
  .contact{position:absolute;top:422px;font-size:7.5px;line-height:10px;color:var(--ink)}
  .wave{position:absolute;left:0;top:415px;width:515px;height:100px}
  .footer-info{position:absolute;left:0;top:482px;width:380px;text-align:center;color:var(--white)}
  .footer-info span{display:block;font-size:10px;line-height:12px}
  .footer-info strong{display:block;font-size:12.5px;font-weight:700;line-height:15px}

  /* New Year front */
  .newyear{background:var(--navy)}
  .newyear .fireworks{position:absolute;inset:0;
    background:
      radial-gradient(circle at 78% 14%,var(--gold-glow),transparent 16%),
      radial-gradient(circle at 14% 30%,var(--gold-glow),transparent 14%),
      radial-gradient(circle at 88% 70%,var(--gold-glow),transparent 14%),
      radial-gradient(circle at 30% 90%,var(--gold-glow),transparent 14%),
      radial-gradient(circle at 40% 10%,var(--snow-glow),transparent 7%),
      radial-gradient(circle at 92% 40%,var(--snow-glow),transparent 7%),
      radial-gradient(circle at 10% 62%,var(--snow-glow),transparent 7%),
      radial-gradient(circle at 62% 92%,var(--snow-glow),transparent 7%),
      radial-gradient(circle at 50% 50%,var(--navy-soft),var(--navy) 70%)}
  .newyear .frame{position:absolute;left:90px;top:90px;width:290px;height:290px;border:4px solid var(--gold);transform:rotate(-12deg)}
  .newyear .wish{position:absolute;left:90px;top:90px;width:290px;height:290px;transform:rotate(-12deg);
    display:flex;flex-direction:column;align-items:center;justify-content:center;font-family:"Fredoka",sans-serif;font-weight:600;text-align:center}
  .wish__line{color:var(--white);font-size:54px;line-height:52px;letter-spacing:1px}
  .wish__year{color:var(--gold);font-size:48px;line-height:48px;border-top:1px solid var(--white);border-bottom:1px solid var(--white);padding:2px 20px;margin-top:6px}
</style>
</head>
<body>

<section class="stage stage--christmas">
  <div class="card-holder" style="left:365px;top:130px">
    <div class="card xmas-front">
      <div class="ornaments" role="img" aria-label="Hängende weiße Schneeflocken-Anhänger und goldene Sterne"></div>
      <div class="greeting greeting--small">Frohe</div>
      <div class="greeting greeting--large">Weihnachten</div>
      <svg class="landscape" viewBox="0 0 515 145" aria-hidden="true">
        <path d="M0 62 Q260 48 515 72 L515 145 L0 145 Z" fill="#ffffff"/>
      </svg>
      <div class="trees" role="img" aria-label="Verschneite Tannen am Horizont"></div>
      <div class="brand"><span class="brand__dot"></span>Kellbrunn</div>
    </div>
  </div>
</section>

<section class="stage stage--spread">
  <div class="card xmas-front" style="left:65px;top:90px">
    <div class="ornaments" role="img" aria-label="Hängende weiße Schneeflocken-Anhänger und goldene Sterne"></div>
    <div class="greeting greeting--small">Frohe</div>
    <div class="greeting greeting--large">Weihnachten</div>
    <svg class="landscape" viewBox="0 0 515 145" aria-hidden="true">
      <path d="M0 62 Q260 48 515 72 L515 145 L0 145 Z" fill="#ffffff"/>
    </svg>
    <div class="trees" role="img" aria-label="Verschneite Tannen am Horizont"></div>
    <div class="brand"><span class="brand__dot"></span>Kellbrunn</div>
  </div>

  <div class="card back" style="left:617px;top:90px">
    <div class="services">
      <div class="service" style="top:26px">
        <svg width="30" height="26" viewBox="0 0 30 26"><path d="M4 13 l8 8 l14 -16" fill="none" stroke="#fff" stroke-width="3" stroke-linecap="round"/></svg>Verkauf</div>
      <div class="service" style="top:116px">
        <svg width="30" height="26" viewBox="0 0 30 26"><path d="M4 13 l8 8 l14 -16" fill="none" stroke="#fff" stroke-width="3" stroke-linecap="round"/></svg>Vermietung</div>
      <div class="service" style="top:200px">
        <svg width="30" height="26" viewBox="0 0 30 26"><path d="M4 13 l8 8 l14 -16" fill="none" stroke="#fff" stroke-width="3" stroke-linecap="round"/></svg>Hausmiet-<br>service</div>
      <div class="service" style="top:300px">
        <svg width="30" height="26" viewBox="0 0 30 26"><path d="M4 13 l8 8 l14 -16" fill="none" stroke="#fff" stroke-width="3" stroke-linecap="round"/></svg>Home<br>Staging</div>
      <div class="service" style="top:398px">
        <svg width="30" height="26" viewBox="0 0 30 26"><path d="M4 13 l8 8 l14 -16" fill="none" stroke="#fff" stroke-width="3" stroke-linecap="round"/></svg>Haus-<br>verwaltung</div>
    </div>

    <div class="brand"><span class="brand__dot"></span><span><small>Nordhaus-Immobilien</small>Kellbrunn</span></div>

    <p class="lead">Für eine <span class="gold">unverbindliche Beratung</span> stehen wir gerne <span class="gold">zur Verfügung</span></p>
    <div class="phone">
      <span class="phone__icon"><svg width="12" height="12" viewBox="0 0 24 24"><path d="M6.6 10.8a15 15 0 0 0 6.6 6.6l2.2-2.2a1 1 0 0 1 1-.25 11.4 11.4 0 0 0 3.6.57 1 1 0 0 1 1 1V20a1 1 0 0 1-1 1A17 17 0 0 1 3 4a1 1 0 0 1 1-1h3.5a1 1 0 0 1 1 1c0 1.25.2 2.45.57 3.57a1 1 0 0 1-.25 1z" fill="#124a7c"/></svg></span>
      <span class="phone__number">012 34 / 56 78 90</span>
    </div>

    <div class="rule" style="left:140px;top:149px;width:345px"></div>
    <h2 class="heading">Wir kümmern uns um <span class="gold">Ihre Immobilie!</span></h2>
    <div class="rule" style="left:140px;top:180px;width:345px"></div>

    <div class="gift">
      <p>Bei Abschluss eines Auftrags<br>schenken wir Ihnen eine „Nuvo“<br>als Weihnachtsgeschenk!</p>
      <p>Aktion gültig bis: 31.01.2019</p>
      <p>Infos unter:<br><span class="link">www.nordhaus-kellbrunn.de</span></p>
    </div>

    <div class="bauble">
      <span class="bauble__string"></span><span class="bauble__cap"></span>
      <span class="bauble__ball">NUVO<br>GRATIS</span>
    </div>

    <div class="portrait" role="img" aria-label="Porträtfoto des Maklerteams"></div>

    <div class="rule" style="left:140px;top:351px;width:212px"></div>
    <p class="invite">Für eine unverbindliche <span class="gold">Beratung</span><br>stehen wir gerne zur Verfügung!</p>
    <div class="rule" style="left:140px;top:392px;width:212px"></div>

    <div class="contact" style="left:140px">Nordhaus-Immobilien<br>Kellbrunn GmbH<br>Lindenweg 4<br>10115 Musterstadt</div>
    <div class="contact" style="left:232px">Tel.: 012 34 / 56 78 90<br>Fax: 012 34 / 56 78 91<br>info@nordhaus-kellbrunn.de<br>www.nordhaus-kellbrunn.de</div>

    <svg class="wave" viewBox="0 0 515 100" preserveAspectRatio="none" aria-hidden="true">
      <path d="M0 74 C190 74 360 56 515 18 L515 30 C360 66 190 82 0 82 Z" fill="#b9954a"/>
      <path d="M0 82 C190 82 360 66 515 30 L515 100 L0 100 Z" fill="#124a7c"/>
    </svg>
    <div class="footer-info"><span>Infos unter:</span><strong>www.nordhaus-kellbrunn.de</strong></div>
  </div>
</section>

<section class="stage stage--newyear">
  <div class="card-holder" style="left:365px;top:160px">
    <div class="card newyear" style="transform:none;width:470px;height:470px">
      <div class="fireworks" role="img" aria-label="Goldene und weiße Feuerwerksfunken und Sterne"></div>
      <div class="frame"></div>
      <div class="wish">
        <span class="wish__line">HAPPY</span>
        <span class="wish__line">NEW</span>
        <span class="wish__line">YEAR</span>
        <span class="wish__year">2019</span>
      </div>
    </div>
  </div>
</section>

</body>
</html>
```